Need a Zine cover designed

I’m looking for someone who can design an eye catching and original zine cover. Incorporating the logo I included below. I’m not 100% sure which logo I want to use on the cover, if it’s possible to see how you incorporate the logos on a sample will make it easier for me to decide. Thank you for your time.
For the second logo I’m unsure how to remove the grey background, but I do not want it included in the zine cover
The title of the zine is:
Amber Crossroads
perspectives of culture, life, & love

```html
<!DOCTYPE html>
<html lang="en">
<head>
<meta charset="utf-8">
<title>Amber Crossroads — Zine Cover</title>
<link rel="stylesheet" href="https://fonts.googleapis.com/css2?family=Archivo:wght@800&family=Nothing+You+Could+Do&display=swap">
<style>
  :root {
    --backdrop: #201f1d;
    --paper: #ffffff;
    --ink: #1d1c1a;
    --accent: #e8313f;
  }
  * { margin: 0; padding: 0; box-sizing: border-box; }
  html, body {
    width: 1200px;
    height: 1200px;
    overflow: hidden;
    background: var(--backdrop);
  }
  .cover {
    position: absolute;
    left: 263px;
    top: 95px;
    width: 674px;
    height: 1010px;
    background: var(--paper);
  }
  .title-line {
    position: absolute;
    font-family: "Archivo", "Helvetica Neue", Arial, sans-serif;
    font-weight: 800;
    font-size: 82px;
    line-height: 1;
    letter-spacing: -3px;
    color: var(--ink);
    white-space: nowrap;
  }
  .title-line--left { right: 357px; text-align: right; }
  .title-line--right { left: 337px; }
  .subtitle-word {
    position: absolute;
    font-family: "Nothing You Could Do", cursive;
    font-size: 36px;
    line-height: 1;
    color: var(--accent);
    white-space: nowrap;
  }
  .club-mark {
    position: absolute;
    left: 0;
    right: 0;
    top: 800px;
    display: flex;
    align-items: center;
    justify-content: center;
    gap: 14px;
  }
  .club-mark__dot {
    width: 30px;
    height: 30px;
    border-radius: 50%;
    background: var(--ink);
  }
  .club-mark__name {
    font-family: "Archivo", "Helvetica Neue", Arial, sans-serif;
    font-weight: 800;
    font-size: 28px;
    letter-spacing: -0.5px;
    color: var(--ink);
  }
</style>
</head>
<body>
  <main class="cover">
    <h1 class="title" aria-label="Amber Crossroads">
      <span class="title-line title-line--left" style="top:172px">AM-</span>
      <span class="title-line title-line--right" style="top:232px">CROSS-</span>
      <span class="title-line title-line--left" style="top:292px">BER</span>
      <span class="title-line title-line--right" style="top:352px">ROADS</span>
    </h1>
    <p class="subtitle" aria-label="perspectives of culture, life, &amp; love">
      <span class="subtitle-word" style="left:28px; top:240px">perspectives</span>
      <span class="subtitle-word" style="left:345px; top:305px">of culture,</span>
      <span class="subtitle-word" style="left:212px; top:355px">life,</span>
      <span class="subtitle-word" style="left:340px; top:410px">&amp; love</span>
    </p>
    <div class="club-mark">
      <span class="club-mark__dot"></span>
      <span class="club-mark__name">Leisure Lounge Club</span>
    </div>
  </main>
</body>
</html>
```